I need an album cover for a hip hop album - Hollow Season is a an album reflecting the post Covid world - Ideas to produce the album cover include desert with dystopian buildings in the background with the words HOLLOW SEASON in between or above.

```html
<!DOCTYPE html>
<html lang="en">
<head>
<meta charset="utf-8">
<title>Hollow Season – Album Cover</title>
<link rel="stylesheet" href="https://fonts.googleapis.com/css2?family=Lexend:wght@600;700&display=swap">
<style>
  :root {
    --page: #ffffff;
    --sleeve: #1f1a07;
    --ink-gold: #9a8519;
    --photo-light: #8a7d1c;
    --photo-mid: #4a4310;
    --photo-dark: #1a1705;
  }
  html, body {
    margin: 0;
    padding: 0;
    width: 1200px;
    height: 574px;
    overflow: hidden;
    background: var(--page);
  }
  .canvas {
    position: relative;
    width: 1200px;
    height: 574px;
    font-family: "Lexend", "Helvetica Neue", Arial, sans-serif;
    color: var(--ink-gold);
  }
  .panel {
    position: absolute;
    top: 54px;
    width: 510px;
    height: 459px;
    background: var(--sleeve);
    overflow: hidden;
  }
  .panel--front { left: 64px; }
  .panel--back { left: 631px; }

  .cover-art {
    position: absolute;
    inset: 0;
    background:
      linear-gradient(180deg, rgba(26,23,5,0) 0%, rgba(26,23,5,0) 40%, var(--photo-dark) 62%),
      linear-gradient(90deg, var(--photo-light) 0%, var(--photo-mid) 35%, var(--photo-light) 62%, var(--photo-dark) 100%);
  }
  .album-title {
    position: absolute;
    left: 0;
    right: 0;
    top: 396px;
    margin: 0;
    text-align: center;
    font-weight: 700;
    font-size: 23px;
    letter-spacing: 0.5px;
    line-height: 1;
  }

  .tracklist {
    position: absolute;
    left: 202px;
    top: 196px;
    margin: 0;
    padding: 0;
    list-style: none;
  }
  .tracklist li {
    font-weight: 700;
    font-size: 21px;
    line-height: 31.2px;
    letter-spacing: -0.2px;
  }
  .footer-note {
    position: absolute;
    top: 427px;
    margin: 0;
    font-weight: 600;
    font-size: 11.5px;
    letter-spacing: 0.4px;
    line-height: 1;
  }
  .footer-note--code { left: 17px; }
  .footer-note--web { right: 21px; }
</style>
</head>
<body>
  <main class="canvas">
    <section class="panel panel--front">
      <div class="cover-art" role="img" aria-label="Photograph of weathered vertical metal panels, lit yellow at the top and fading into dark stains below"></div>
      <h1 class="album-title">HOLLOW SEASON</h1>
    </section>

    <section class="panel panel--back">
      <ol class="tracklist">
        <li>SONG NAME</li>
        <li>SONG NAME</li>
        <li>SONG NAME</li>
        <li>SONG NAME</li>
        <li>SONG NAME</li>
      </ol>
      <p class="footer-note footer-note--code">QR CODE AND/ OR BARCODE</p>
      <p class="footer-note footer-note--web">WWW.WEBSITENAME.COM</p>
    </section>
  </main>
</body>
</html>
```